Website Landing Page for Brightfall Systems

Create a custom designed website landing page for our business. Looking for a professional upscale design that incorporates our logo and logo colors into the theme. I want a standard fixed frame website, not a constant scrolling format that seems to be the trend. To start with I'm looking for more of the graphic design part, maybe a concept or theme, I don't expect to see a finished project. Not interested in generic templates or layouts.

The name of our company is Brightfall Systems and I've attached our logo below. I'd like to have the web page have the same look and feel of our logo, as well as the colors. Our company, Brightfall Systems does system design, installation, and programming, of residential and commercial Audio/Video and Automation systems. We do home theaters, lighting and building automation, video conferencing systems, security camera installations, conference rooms, projectors, distributed audio systems, and similar Technology projects. This will be a professional services/informational website. We will not sell products on this website. This website will be used to advertise our company and communicate our services to prospective customers. Having a well designed, professional and clean website is one way we want to distinguish our company from the competition.

Here are some examples of what I consider a professional well designed website
http://www.qorlamstudio.com/Work/

Last year we had our tradlo store designed (with PixelMarket) and I'm really happy with the way it turned out. You can see it at www.HolvenGearDepot.com I consider this to be a great design and looking for the same level of quality with this new website. However, do not copy or use any part of this design in this new project. This tradlo store is completely separate from our other company Brightfall Systems. I only mention this tradlo store an an example of good work.

Reason: Still going through designs.

Reason: Still working on project and have not had time to review all designs and request revisions.

Reason: Sill going through designs and requesting revisions

Reason: still going through all the submissions we received.

Target Market(s)

People interested in Audio/Video, home theaters, home automation. We do sales, system design, and programming. We typically work on larger projects with both residential and commercial customers.

Industry/Entity Type

Business

Number of Pages Required

1 page

Requirements
Must have
• Great design elements. Please use a white background. I think white goes well with our logo colors.

```html
<!DOCTYPE html>
<html lang="en">
<head>
<meta charset="utf-8">
<title>Brightfall Systems</title>
<link rel="stylesheet" href="https://fonts.googleapis.com/css2?family=Oswald:wght@300;400&family=Lato:wght@400;700&family=Open+Sans:wght@400;600&display=swap">
<style>
:root{
  --blue:#3b7fcc;
  --green:#5cb648;
  --ink:#222;
  --body:#555;
  --footer:#d7d7d7;
  --white:#fff;
}
*{box-sizing:border-box;margin:0;padding:0}
html,body{width:1200px;height:5325px;overflow:hidden}
body{background:var(--white);font-family:"Open Sans",Arial,sans-serif;color:var(--body);position:relative}
section,header,footer{position:absolute;left:0;width:1200px}
.heading{font-family:"Oswald",Arial,sans-serif;font-weight:400;color:var(--ink);font-size:72px;line-height:1;text-transform:uppercase}
.rule{width:60px;height:3px;background:var(--ink);margin:22px 0 20px}
.lead{font-size:15px;line-height:1.55;width:330px;color:#333}
.btn-outline{display:inline-block;margin-top:32px;width:200px;height:56px;border:2px solid var(--ink);font-size:13px;text-transform:uppercase;text-align:center;line-height:52px;color:var(--ink)}
.btn-blue{display:block;margin:0 auto;width:280px;height:72px;background:var(--blue);color:#fff;text-align:center;line-height:72px;font-family:"Lato",sans-serif;font-size:17px;text-transform:uppercase}

/* hero */
.hero{top:0;height:685px;background:linear-gradient(180deg,#3a3a3a 0%,#5b5753 45%,#2b2a29 100%)}
.brand-small{position:absolute;left:60px;top:40px;font-family:"Lato",sans-serif;font-weight:700;font-size:14px;color:var(--green);text-transform:uppercase}
.nav{position:absolute;right:58px;top:44px;display:flex;gap:42px;font-size:13px;color:#fff}
.hero-title{position:absolute;left:120px;top:200px;font-family:"Oswald",sans-serif;font-size:74px;line-height:1.1;color:#fff;text-transform:uppercase}
.hero-title .b{color:var(--blue)}.hero-title .g{color:var(--green)}
.hero-sub{position:absolute;left:120px;top:415px;width:380px;color:#fff;font-size:17px;line-height:1.45}
.chevron{position:absolute;left:566px;top:570px}

/* about */
.about{top:685px;height:717px}
.about .text{position:absolute;left:175px;top:215px}
.brand-name{position:absolute;left:680px;top:300px;width:420px;text-align:center;font-family:"Oswald",sans-serif;font-weight:400;font-size:44px;line-height:1;color:var(--ink);text-transform:uppercase}

/* banners */
.banner{color:#fff;text-align:center}
.banner h2{font-family:"Lato",sans-serif;font-weight:400;font-size:40px;line-height:1.2;text-transform:uppercase;margin-bottom:40px}
.banner-one{top:1402px;height:391px;background:linear-gradient(180deg,#1a1a1a,#3c3c3c 55%,#1d1d1d);padding-top:120px}
.banner-two{top:2510px;height:394px;background:linear-gradient(180deg,#151515,#4a4238 55%,#222);padding-top:125px}
.banner-three{top:3621px;height:391px;background:linear-gradient(180deg,#111,#2e2e2e 60%,#1a1a1a);padding-top:85px}

/* services */
.services{top:1793px;height:717px}
.services .text{position:absolute;left:175px;top:215px}
.service-grid{position:absolute;left:640px;top:190px;display:grid;grid-template-columns:250px 250px;row-gap:40px;text-align:center;font-size:14px;color:#333;text-transform:uppercase}
.service-grid svg{display:block;margin:0 auto 10px}

/* call */
.call{top:2904px;height:717px}
.call .text{position:absolute;left:175px;top:215px}
.call .lead{font-size:13px;width:400px;margin-bottom:16px}
.agent{position:absolute;left:765px;top:165px;width:200px;height:230px;border-radius:100px 100px 30px 30px;background:linear-gradient(180deg,#e5eef9,#c9dbf1)}
.phone-btn{position:absolute;left:790px;top:420px;width:150px;height:38px;border-radius:6px;background:var(--green);color:#fff;font-weight:600;font-size:15px;text-align:center;line-height:38px}

/* testimonials */
.testimonials{top:4012px;height:720px}
.testimonials .text{position:absolute;left:175px;top:200px}
.testimonials .lead{font-size:17px;line-height:1.4}
.arrow{position:absolute;top:210px}
.quote{position:absolute;left:680px;top:140px;width:400px;text-align:center}
.avatar{width:200px;height:200px;border-radius:50%;margin:0 auto 28px;background:linear-gradient(180deg,#cfe0ee,#9fb7c8)}
.quote h3{font-family:"Lato",sans-serif;font-weight:700;font-size:24px;color:#333}
.quote .role{font-size:17px;color:#555;margin:4px 0 22px;white-space:nowrap}
.quote p{font-size:13px;line-height:1.5;color:#777;padding:0 40px}

/* footer */
.footer{top:4732px;height:558px;background:var(--footer);font-size:13px;color:#333}
.foot-brand{position:absolute;left:90px;top:110px}
.foot-brand .name{font-family:"Lato",sans-serif;font-weight:700;font-size:14px;color:var(--ink);text-transform:uppercase;margin-bottom:14px}
.foot-brand p{line-height:1.5}
.socials{display:flex;gap:6px;margin-top:10px}
.socials span{width:28px;height:28px;background:var(--blue)}
.foot-col{position:absolute;top:70px}
.foot-col h4{font-weight:600;font-size:14px;text-transform:uppercase;margin-bottom:14px;color:#111}
.foot-col li{list-style:none;line-height:1.6}
.services-col{left:405px}
.blog-col{left:675px;width:420px}
.post{display:flex;gap:14px;margin-bottom:22px}
.post .thumb{flex:none;width:80px;height:76px;background:linear-gradient(135deg,#8a8f96,#c7c2ba)}
.post b{display:block;font-size:13px;margin-bottom:4px}
.post p{font-size:12px;line-height:1.4;color:#555}
.bottom-bar{position:absolute;left:0;top:5290px;width:1200px;height:35px;background:var(--blue);color:#fff;font-size:12px;line-height:35px;padding-left:90px}
.bottom-bar u{margin-left:6px}
</style>
</head>
<body>

<header class="hero" role="img" aria-label="Photograph of a modern conference room with a long table and leather chairs">
  <div class="brand-small">Brightfall Systems</div>
  <nav class="nav"><span>About</span><span>Why?</span><span>Solutions</span><span>Contact Us</span><span>Blog</span>
    <svg width="14" height="14" viewBox="0 0 14 14"><circle cx="6" cy="6" r="4.5" fill="none" stroke="#fff" stroke-width="1.5"/><line x1="9.5" y1="9.5" x2="13" y2="13" stroke="#fff" stroke-width="1.5"/></svg></nav>
  <h1 class="hero-title"><span class="b">Less</span> Downtime,<br><span class="g">More</span> Productivity</h1>
  <p class="hero-sub">Wave goodbye to the headaches caused by poorly functioning and ineffectual IT</p>
  <svg class="chevron" width="68" height="40" viewBox="0 0 68 40"><polyline points="6,6 34,32 62,6" fill="none" stroke="#111" stroke-width="8"/></svg>
</header>

<section class="about">
  <div class="text">
    <h2 class="heading">About Us</h2>
    <div class="rule"></div>
    <p class="lead">Lorem ipsum dolor sit amet, consectetur adipiscing elit. Integer finibus lorem vitae nulla fringilla luctus.</p>
    <span class="btn-outline">Learn More</span>
  </div>
  <div class="brand-name">Brightfall Systems</div>
</section>

<section class="banner banner-one" role="img" aria-label="Photograph of a large auditorium with a projection screen">
  <h2>Lorem ipsum dolor sit amet?</h2>
  <span class="btn-blue">Yes Please</span>
</section>

<section class="services">
  <div class="text">
    <h2 class="heading">Services</h2>
    <div class="rule"></div>
    <p class="lead">Lorem ipsum dolor sit amet, consectetur adipiscing elit. Integer finibus lorem vitae nulla fringilla luctus.</p>
    <span class="btn-outline">See More</span>
  </div>
  <div class="service-grid">
    <div><svg width="64" height="64" viewBox="0 0 64 64"><circle cx="32" cy="32" r="18" fill="none" stroke="var(--blue)" stroke-width="6" stroke-dasharray="8 4"/><circle cx="32" cy="32" r="7" fill="var(--blue)"/></svg>Automation Systems</div>
    <div><svg width="64" height="64" viewBox="0 0 64 64"><rect x="8" y="10" width="48" height="44" rx="3" fill="var(--blue)"/><rect x="13" y="20" width="38" height="29" fill="#fff"/><text x="32" y="40" font-size="14" text-anchor="middle" fill="var(--blue)" font-family="Open Sans,sans-serif">&lt;/&gt;</text></svg>Programming</div>
    <div><svg width="64" height="64" viewBox="0 0 64 64"><rect x="10" y="8" width="44" height="28" fill="none" stroke="var(--blue)" stroke-width="4"/><rect x="6" y="40" width="14" height="16" fill="var(--blue)"/><rect x="44" y="40" width="14" height="16" fill="var(--blue)"/><rect x="24" y="44" width="16" height="10" fill="var(--blue)"/></svg>Home Theater</div>
    <div><svg width="64" height="64" viewBox="0 0 64 64"><rect x="14" y="16" width="40" height="18" rx="3" transform="rotate(15 34 25)" fill="var(--blue)"/><rect x="10" y="40" width="6" height="18" fill="var(--blue)"/><line x1="13" y1="44" x2="24" y2="34" stroke="var(--blue)" stroke-width="5"/></svg>Security Camera<br>Installations</div>
  </div>
</section>

<section class="banner banner-two" role="img" aria-label="Photograph of a dim home theater room with seating">
  <h2>Lorem ipsum dolor sit amet?</h2>
  <span class="btn-blue">Lorem Ipsum</span>
</section>

<section class="call">
  <div class="text">
    <h2 class="heading">Call Us</h2>
    <div class="rule"></div>
    <p class="lead">Lorem ipsum dolor sit amet, consectetur adipiscing elit. Integer finibus lorem vitae nulla fringilla luctus. Mauris eget metus nec dictum, vestibulum lectus sit placerat magna. In hac habitasse platea dictumst.</p>
    <p class="lead">Donec eu placerat metus, quis placerat lorem. Proin ornare augue.</p>
  </div>
  <div class="agent" role="img" aria-label="Line illustration of a support agent wearing a headset"></div>
  <div class="phone-btn">555-201-4410</div>
</section>

<section class="banner banner-three" role="img" aria-label="Photograph of a laptop and an open notebook on a desk">
  <h2>Lorem ipsum dolor sit amet,<br>consectetur adipiscing elit.</h2>
  <span class="btn-blue">Learn More</span>
</section>

<section class="testimonials">
  <div class="text">
    <h2 class="heading">Testimonials</h2>
    <div class="rule"></div>
    <p class="lead">The Highest Standards.<br>The happiest customers</p>
  </div>
  <svg class="arrow" style="left:628px" width="40" height="70" viewBox="0 0 40 70"><polyline points="32,6 8,35 32,64" fill="none" stroke="var(--green)" stroke-width="10"/></svg>
  <svg class="arrow" style="left:1000px" width="40" height="70" viewBox="0 0 40 70"><polyline points="8,6 32,35 8,64" fill="none" stroke="var(--green)" stroke-width="10"/></svg>
  <div class="quote">
    <div class="avatar" role="img" aria-label="Portrait photograph of the client"></div>
    <h3>Dan Morrow</h3>
    <div class="role">General Manager at Ridgeline Landscaping</div>
    <p>Lorem ipsum dolor sit amet, consectetur adipiscing elit, sed do eiusmod tempor incididunt ut labore et dolore magna aliqua. Ut enim ad minim veniam, quis nostrud exercitation ullamco laboris nisi ut aliquip ex ea commodo consequat.</p>
  </div>
</section>

<footer class="footer">
  <div class="foot-brand">
    <div class="name">Brightfall Systems</div>
    <p>2290 Harlow Street<br>Fairview, IL 60000<br>555-201-4477</p>
    <div class="socials"><span></span><span></span></div>
  </div>
  <div class="foot-col services-col">
    <h4>IT Services</h4>
    <ul><li>System Design</li><li>Installation</li><li>Programming</li><li>Audio/Video</li><li>Automation Systems</li><li>Home Theater</li><li>Lighting and Building Automation</li><li>Video Conferencing Systems</li><li>Security Camera Installations</li><li>Conference Rooms</li><li>Distributed Audio Systems</li><li>Projectors</li></ul>
  </div>
  <div class="foot-col blog-col">
    <h4>Blog</h4>
    <div class="post"><div class="thumb" role="img" aria-label="Blog post photograph"></div><div><b>Lorem ipsum dolor sit amet cons...</b><p>Lorem ipsum dolor sit amet, consectetur adipiscing elit, sed do eiusmod tempor incididunt ut labore et dolore magna aliqua.</p></div></div>
    <div class="post"><div class="thumb" role="img" aria-label="Blog post photograph"></div><div><b>Lorem ipsum dolor sit amet cons...</b><p>Lorem ipsum dolor sit amet, consectetur adipiscing elit, sed do eiusmod tempor incididunt ut labore et dolore magna aliqua.</p></div></div>
    <div class="post"><div class="thumb" role="img" aria-label="Blog post photograph"></div><div><b>Lorem ipsum dolor sit amet cons...</b><p>Lorem ipsum dolor sit amet, consectetur adipiscing elit, sed do eiusmod tempor incididunt ut labore et dolore magna aliqua.</p></div></div>
  </div>
</footer>
<div class="bottom-bar">Copyright © 2017. All rights reserved. <u>Privacy &amp; Policy</u></div>

</body>
</html>
```